Brand new website for global research and investment startup

We need a simple website, maybe 3 pages: landing page with business description, investment philosophy, team and contact info.
We have a logo already that can be incorporated. Please use the logo only, not the text
We like the color green, something along the lines of #3D6C32 as the main color.
We'd like to design the website with geometric shapes in gradations of the base color. The shapes should suggest "work in progress", "built to last (a long time)", "solidity" and "indestructibility". One idea floating in my head sees smaller features with icosahedron and dodecahedron shapes, and maybe larger structures like crystal lattices; but please feel free to be creative and imagine your own.

```html
<!DOCTYPE html>
<html lang="en">
<head>
<meta charset="utf-8">
<title>Cedarline Research Capital</title>
<link rel="stylesheet" href="https://fonts.googleapis.com/css2?family=Manrope:wght@500;600;700&family=Inter:wght@400;500;600;700&display=swap">
<style>
:root{
  --green:#3d6c32;
  --green-dark:#2c5a31;
  --green-deep:#234a28;
  --green-bright:#5aa53a;
  --green-light:#4c8f35;
  --tint:#f6f8f2;
  --chip:#e3eedb;
  --ink:#1c1c1c;
  --muted:#6a6a6a;
  --rule:#dcdcdc;
  --white:#ffffff;
}
*{margin:0;padding:0;box-sizing:border-box}
html,body{width:1200px;height:4132px;overflow:hidden}
body{font-family:"Inter",sans-serif;color:var(--ink);background:var(--white);position:relative}
.section{position:absolute;left:0;width:1200px}
.h-display{font-family:"Manrope",sans-serif;font-weight:600;color:var(--green-dark);text-transform:uppercase;letter-spacing:.5px}
.eyebrow{font-size:14px;letter-spacing:.6px;color:var(--green-light);text-transform:uppercase;font-weight:500}

/* hero */
.hero{top:0;height:680px;background:linear-gradient(180deg,#1a6fc4 0%,#3d8fd6 30%,#8fc1e6 45%,#1f9fb8 52%,#49b8c4 62%,#cfe3e0 74%,#e9dcc5 82%,#dcc8a8 100%)}
.hero-photo{position:absolute;inset:0}
.site-header{position:absolute;top:0;left:0;width:1200px;height:88px;border-bottom:1px solid rgba(255,255,255,.3);display:flex;align-items:center}
.brand{position:absolute;left:120px;top:30px;display:flex;align-items:center;gap:10px;color:var(--white);font-family:"Manrope",sans-serif;font-weight:700;font-size:20px}
.brand-dot{width:26px;height:26px;border-radius:50%;background:var(--white)}
.main-nav{position:absolute;left:447px;top:36px;display:flex;gap:25px}
.main-nav a{color:var(--white);text-decoration:none;font-size:12px;font-weight:600;letter-spacing:.3px}
.btn{display:inline-flex;align-items:center;justify-content:center;gap:12px;border-radius:30px;font-weight:600;text-decoration:none}
.btn-solid{background:linear-gradient(90deg,var(--green) 0%,var(--green-bright) 100%);color:var(--white)}
.btn-header{position:absolute;left:928px;top:26px;width:152px;height:36px;font-size:12px}
.hero-frame{position:absolute;left:321px;top:230px;width:559px;height:180px;border:1.5px solid rgba(255,255,255,.85);border-top:none}
.hero-frame::before,.hero-frame::after{content:"";position:absolute;top:0;height:1.5px;background:rgba(255,255,255,.85);width:190px}
.hero-frame::before{left:0}.hero-frame::after{right:0}
.hero-kicker{position:absolute;left:0;width:1200px;top:218px;text-align:center;color:var(--white);font-size:21px;letter-spacing:1px}
.hero-title{position:absolute;left:0;width:1200px;top:258px;text-align:center;color:var(--white);font-family:"Manrope",sans-serif;font-weight:600;font-size:40px;line-height:46px;letter-spacing:.5px}
.btn-hero{position:absolute;left:500px;top:382px;width:200px;height:56px;font-size:15px;background:linear-gradient(90deg,var(--green-dark),var(--green-bright))}

/* values */
.values{top:680px;height:416px}
.value{position:absolute;top:64px;width:328px;text-align:center}
.value-divider{position:absolute;top:64px;width:1px;height:282px;background:var(--rule)}
.value-icon{width:128px;height:128px;margin:8px auto 0;display:block}
.value h3{font-family:"Manrope",sans-serif;font-weight:700;font-size:20px;letter-spacing:.5px;margin-top:27px}
.value p{font-size:12px;line-height:17px;color:var(--muted);margin:12px auto 0;width:228px}

/* about */
.about{top:1096px;height:405px;background:var(--tint)}
.about .eyebrow{position:absolute;left:120px;top:74px}
.about h2{position:absolute;left:120px;top:104px;font-size:37px;line-height:45px}
.about-copy{position:absolute;left:610px;top:70px;width:412px;font-size:13px;line-height:21px;color:#444}
.about-copy strong{font-weight:600;color:var(--ink)}
.about-copy p+p{margin-top:21px}
.btn-outline{position:absolute;left:610px;top:284px;width:216px;height:47px;border:1.5px solid var(--green-dark);color:var(--green-dark);font-size:13px}

/* philosophy */
.philosophy{top:1501px;height:820px}
.philosophy .eyebrow{position:absolute;left:0;width:1200px;text-align:center;top:69px}
.philosophy h2{position:absolute;left:0;width:1200px;text-align:center;top:98px;font-size:38px;line-height:45px}
.wave-photo{position:absolute;left:120px;top:227px;width:464px;height:520px;background:linear-gradient(160deg,#3f7fc9 0%,#6cb0e3 35%,#e8f3f7 48%,#2a7db5 60%,#12477f 100%)}
.principle{position:absolute;left:632px;width:449px}
.principle-num{display:inline-block;background:var(--chip);color:var(--green);font-size:14px;padding:3px 6px;border-radius:3px}
.principle h3{font-family:"Manrope",sans-serif;font-weight:700;font-size:20px;margin-top:10px;letter-spacing:.3px}
.principle p{font-size:11px;line-height:17px;color:var(--muted);margin-top:8px}
.principle-rule{position:absolute;left:632px;width:449px;height:1px;background:var(--rule)}

/* credo */
.credo{top:2321px;height:279px;background:var(--green-dark);text-align:center;color:var(--white)}
.credo blockquote{position:absolute;left:0;width:1200px;top:62px;font-family:"Manrope",sans-serif;font-weight:500;font-size:37px;line-height:47px}
.credo cite{position:absolute;left:0;width:1200px;top:188px;font-style:normal;font-size:11px;font-weight:600;letter-spacing:.3px}

/* team */
.team{top:2600px;height:1130px}
.team h2{position:absolute;left:0;width:1200px;text-align:center;top:64px;font-size:38px}
.member-photo{position:absolute;left:120px;width:480px;height:360px}
.photo-a{background:linear-gradient(90deg,#d8dbd6 0%,#b9bfb7 40%,#3a3d45 60%,#e4e6e2 100%)}
.photo-b{background:linear-gradient(90deg,#cfd2cf 0%,#e6e8e6 35%,#2f3136 55%,#dfe2e0 100%)}
.member-name{position:absolute;left:120px;width:480px;text-align:center;font-family:"Manrope",sans-serif;font-weight:600;font-size:24px;letter-spacing:.5px}
.member-role{position:absolute;left:120px;width:480px;text-align:center;font-size:12px;font-weight:600;color:var(--green)}
.member-bio{position:absolute;left:640px;width:412px;font-size:12.5px;line-height:21px;color:#666;text-align:justify}
.member-bio p+p{margin-top:21px}

/* footer */
.site-footer{top:3730px;height:357px;background:var(--tint)}
.footer-brand{position:absolute;left:120px;top:74px;display:flex;align-items:center;gap:10px;font-family:"Manrope",sans-serif;font-weight:700;font-size:20px;color:var(--green-dark)}
.footer-brand .brand-dot{background:var(--green-dark)}
.footer-about{position:absolute;left:120px;top:140px;width:290px;font-size:11px;line-height:18px;color:#666}
.socials{position:absolute;left:120px;top:214px;display:flex;gap:5px}
.socials span{width:30px;height:30px;border-radius:50%;background:var(--green-light)}
.footer-col h4{position:absolute;top:72px;font-family:"Inter",sans-serif;font-weight:500;font-size:16px}
.footer-col h4::after{content:"";position:absolute;left:0;top:28px;width:24px;height:2px;background:var(--green)}
.footer-nav{position:absolute;left:562px;top:132px;list-style:none}
.footer-nav li{font-size:11px;line-height:29.5px;padding-left16px;}
.footer-nav li::before{content:"•";margin-right:12px;font-size:10px}
.contact-list{position:absolute;left:856px;top:130px;list-style:none}
.contact-list li{display:flex;gap:12px;font-size:11px;line-height:16px;margin-bottom:18px}
.contact-list svg{flex:none;margin-top:1px}
.legal{position:absolute;top:4087px;left:0;width:1200px;height:45px;background:var(--green-dark);color:var(--white);font-size:11px;text-align:center;line-height:45px}
</style>
</head>
<body>

<section class="section hero">
  <div class="hero-photo" role="img" aria-label="Photograph of a calm turquoise sea meeting a sandy beach under a bright blue sky"></div>
  <header class="site-header">
    <div class="brand"><span class="brand-dot"></span>Cedarline</div>
    <nav class="main-nav">
      <a href="#">HOME</a><a href="#">PHILOSOPHY</a><a href="#">INSIGHTS</a><a href="#">BLOG</a><a href="#">TEAM</a><a href="#">CONTACT</a>
    </nav>
    <a class="btn btn-solid btn-header" href="#">GET STARTED
      <svg width="8" height="12" viewBox="0 0 8 12"><path d="M2 1l5 5-5 5" fill="none" stroke="#fff" stroke-width="1.8"/></svg></a>
  </header>
  <div class="hero-frame"></div>
  <p class="hero-kicker">WELCOME TO</p>
  <h1 class="hero-title">CEDARLINE RESEARCH<br>CAPITAL</h1>
  <a class="btn btn-hero" href="#">LEARN MORE
    <svg width="8" height="13" viewBox="0 0 8 13"><path d="M2 1l5 5.5-5 5.5" fill="none" stroke="#fff" stroke-width="1.8"/></svg></a>
</section>

<section class="section values">
  <div class="value" style="left:107px">
    <svg class="value-icon" viewBox="0 0 128 128"><circle cx="64" cy="64" r="61" fill="none" stroke="#3d6c32" stroke-width="5"/>
      <path d="M64 92 C36 72 34 58 38 50 C43 40 56 40 64 50 C72 40 85 40 90 50 C94 58 92 72 64 92Z" fill="none" stroke="#2c5a31" stroke-width="3"/>
      <path d="M50 66 l10 -8 14 10 M56 74 l8 6 M62 70 l8 6" fill="none" stroke="#2c5a31" stroke-width="3" stroke-linecap="round"/></svg>
    <h3>INTEGRITY</h3>
    <p>Lorem ipsum dolor sit amet consectetur adipiscing elit, sed do eiusmod tempor incididunt magna aliqua.</p>
  </div>
  <div class="value-divider" style="left:434px"></div>
  <div class="value" style="left:435px">
    <svg class="value-icon" viewBox="0 0 128 128"><circle cx="64" cy="64" r="61" fill="none" stroke="#3d6c32" stroke-width="5"/>
      <circle cx="58" cy="60" r="18" fill="none" stroke="#2c5a31" stroke-width="3"/><circle cx="70" cy="68" r="18" fill="none" stroke="#2c5a31" stroke-width="3"/>
      <path d="M54 72 l22 -22 M60 78 l20 -20 M48 64 l20 -20" stroke="#2c5a31" stroke-width="2"/></svg>
    <h3>TRANSPARENCY</h3>
    <p>Lorem ipsum dolor sit amet consectetur adipiscing elit, sed do eiusmod tempor incididunt magna aliqua.</p>
  </div>
  <div class="value-divider" style="left:764px"></div>
  <div class="value" style="left:763px">
    <svg class="value-icon" viewBox="0 0 128 128"><circle cx="64" cy="64" r="61" fill="none" stroke="#3d6c32" stroke-width="5"/>
      <g fill="none" stroke="#2c5a31" stroke-width="3"><rect x="38" y="68" width="9" height="18"/><rect x="52" y="60" width="9" height="26"/><rect x="66" y="52" width="9" height="34"/><rect x="80" y="44" width="9" height="42"/>
      <path d="M36 60 L58 44 L68 50 L88 34 M80 34 h8 v8"/><path d="M32 88 h64"/></g></svg>
    <h3>EFFICIENCY</h3>
    <p>Lorem ipsum dolor sit amet consectetur adipiscing elit, sed do eiusmod tempor incididunt magna aliqua.</p>
  </div>
</section>

<section class="section about">
  <p class="eyebrow">WHO WE ARE</p>
  <h2 class="h-display">WE INVEST IN THE<br>FUTURES THAT<br>MATTER MOST.</h2>
  <div class="about-copy">
    <p><strong>Stillwater Holdings is a private investment firm built on the conviction that lasting financial success and meaningful human relationships are not in tension — they are inseparable.</strong></p>
    <p>We work with a small number of carefully selected families, foundations, and professional investors — investing side by side across private equity, real assets, and long-term growth companies. No mass-marketing. Only face-to-face relationships built on trust.</p>
  </div>
  <a class="btn btn-outline" href="#">Learn how we invest
    <svg width="7" height="11" viewBox="0 0 7 11"><path d="M1.5 1l4 4.5-4 4.5" fill="none" stroke="#2c5a31" stroke-width="1.6"/></svg></a>
</section>

<section class="section philosophy">
  <p class="eyebrow">INVESTMENT PHILOSOPHY</p>
  <h2 class="h-display">THREE PRINCIPLES.<br>ONE ENDURING BELIEF.</h2>
  <div class="wave-photo" role="img" aria-label="Photograph of a large blue ocean wave curling and breaking"></div>
  <div class="principle" style="top:253px">
    <span class="principle-num">01</span>
    <h3>PATIENT CAPITAL</h3>
    <p>We invest for generations, not quarters. The most meaningful growth happens on a horizon measured in decades, not earnings cycles. Our positions are held for 7 to 15 years — or longer, when a business warrants it.</p>
  </div>
  <div class="principle-rule" style="top:398px"></div>
  <div class="principle" style="top:431px">
    <span class="principle-num">02</span>
    <h3>SHARED JOURNEY</h3>
    <p>We invest alongside every client. When we recommend an opportunity, our own capital is already committed. This alignment is non-negotiable — it ensures our interests remain perfectly matched at every stage.</p>
  </div>
  <div class="principle-rule" style="top:576px"></div>
  <div class="principle" style="top:609px">
    <span class="principle-num">03</span>
    <h3>PURPOSEFUL GROWTH</h3>
    <p>Capital should serve life. Every investment we make considers its effect on people, communities, and the natural world. We believe the most enduring value is created by companies that make things genuinely better.</p>
  </div>
</section>

<section class="section credo">
  <blockquote>"The most important investments are the<br>ones that outlast the investor."</blockquote>
  <cite>STILLWATER HOLDINGS · INVESTMENT CREDO</cite>
</section>

<section class="section team">
  <h2 class="h-display">THE TEAM</h2>
  <div class="member-photo photo-a" style="top:138px" role="img" aria-label="Portrait photograph of a senior partner in a dark suit and red tie"></div>
  <p class="member-name" style="top:524px">ARTHUR VALE</p>
  <p class="member-role" style="top:563px">PARTNER</p>
  <div class="member-bio" style="top:172px">
    <p>Lorem ipsum dolor sit amet, consectetur adipisicing elit, sed do eiusmod tempor incididunt ut labore et dolore magna aliqua. Ut enim ad minim veniam, quis nostrud exercitation ullamco laboris nisi ut aliquip ex ea commodo consequat.</p>
    <p>Duis aute irure dolor in reprehenderit in voluptate velit esse cillum dolore eu fugiat nulla pariatur. Excepteur sint occaecat cupidatat non proident, sunt in culpa qui officia deserunt mollit anim id est laborum. Sed ut perspiciatis unde omnis iste natus error sit voluptatem accusantium doloremque laudantium, totam rem aperiam, eaque ipsa quae ab illo inventore veritatis et quasi architecto beatae vitae dicta sunt explicabo. Nemo enim ipsam voluptatem quia voluptas sit aspernatur aut odit aut fugit, sed quia consequuntur magni dolores eos qui ratione.</p>
  </div>
  <div class="member-photo photo-b" style="top:622px" role="img" aria-label="Portrait photograph of a partner in a dark suit and tie in a bright office"></div>
  <p class="member-name" style="top:1007px">MARCUS REED</p>
  <p class="member-role" style="top:1046px">PARTNER</p>
  <div class="member-bio" style="top:655px">
    <p>Lorem ipsum dolor sit amet, consectetur adipisicing elit, sed do eiusmod tempor incididunt ut labore et dolore magna aliqua. Ut enim ad minim veniam, quis nostrud exercitation ullamco laboris nisi ut aliquip ex ea commodo consequat.</p>
    <p>Duis aute irure dolor in reprehenderit in voluptate velit esse cillum dolore eu fugiat nulla pariatur. Excepteur sint occaecat cupidatat non proident, sunt in culpa qui officia deserunt mollit anim id est laborum. Sed ut perspiciatis unde omnis iste natus error sit voluptatem accusantium doloremque laudantium, totam rem aperiam, eaque ipsa quae ab illo inventore veritatis et quasi architecto beatae vitae dicta sunt explicabo. Nemo enim ipsam voluptatem quia voluptas sit aspernatur aut odit aut fugit, sed quia consequuntur magni dolores eos qui ratione.</p>
  </div>
</section>

<footer class="section site-footer">
  <div class="footer-brand"><span class="brand-dot"></span>Cedarline</div>
  <p class="footer-about">Cedarline Research Capital is a private investment firm for select families and institutions. Geneva — by appointment only.</p>
  <div class="socials" aria-label="Social links"><span></span><span></span><span></span><span></span></div>
  <div class="footer-col"><h4 style="left:558px">NAVIGATE</h4></div>
  <ul class="footer-nav">
    <li>HOME</li><li>PHILOSOPHY</li><li>INSIGHTS</li><li>BLOG</li><li>TEAM</li><li>CONTACT</li>
  </ul>
  <div class="footer-col"><h4 style="left:854px">CONTACT US</h4></div>
  <ul class="contact-list">
    <li><svg width="11" height="14" viewBox="0 0 11 14"><path d="M5.5 13.5C2 9 1 7 1 5a4.5 4.5 0 019 0c0 2-1 4-4.5 8.5z" fill="#2c5a31"/><circle cx="5.5" cy="5" r="1.6" fill="#f6f8f2"/></svg><span>4120 Lorem Way #210<br>Ipsum dolor, NV 89012</span></li>
    <li><svg width="12" height="12" viewBox="0 0 12 12"><path d="M2.5 1l2 2.5-1.2 1.3a7 7 0 003.9 3.9L8.5 7.5 11 9.5 9.8 11C5 11 1 7 1 2.2z" fill="#2c5a31"/></svg><span>+88 555 010 246</span></li>
    <li><svg width="12" height="10" viewBox="0 0 12 10"><rect x="0.5" y="0.5" width="11" height="9" rx="1" fill="#2c5a31"/><path d="M1 1.5l5 4 5-4" fill="none" stroke="#f6f8f2" stroke-width="1"/></svg><span>hello@cedarlinecapital.com</span></li>
  </ul>
</footer>
<p class="legal">© 2024 Cedarline Research Capital. All rights reserved.</p>

</body>
</html>
```